Corvath Holdings, LLC

We are a design build general contracting company.
We work with commercial accounts and private developers. We build retail spaces, restaurants and housing projects.
Im looking for a clean professional type of logo incorporating a roman flavor, think ionic columns and pedestals.
Two toned colorway.
I like unusual fonts and Im not afraid to do something bold with the logo.
Contact Information for Business Card
Marisol Brenkowitz
318-472-9051 corvathmb@mailvexo.com
Font styles to use
Decorative
Colors
Designer to choose colors to be used in the design.
Requirements
Should not have
- I don't like reds pinks.

```html
<!DOCTYPE html>
<html lang="en">
<head>
<meta charset="UTF-8">
<title>Corvath Holdings, LLC — Business Card</title>
<link rel="stylesheet" href="https://fonts.googleapis.com/css2?family=Arimo:wght@400;700&display=swap">
<style>
  :root {
    --page: #e9e6e1;
    --card-white: #ffffff;
    --ink: #0a0a0a;
    --gold: #d3a92c;
    --light: #ffffff;
  }
  * { margin: 0; padding: 0; box-sizing: border-box; }
  html, body {
    width: 1200px;
    height: 902px;
    overflow: hidden;
    background: var(--page);
    font-family: "Arimo", Arial, sans-serif;
  }
  .card {
    position: absolute;
    left: 100px;
    top: 166px;
    width: 1000px;
    height: 570px;
    background: var(--card-white);
    overflow: hidden;
    box-shadow: 0 6px 24px rgba(0,0,0,0.18);
  }
  .card__swoosh {
    position: absolute;
    inset: 0;
    width: 1000px;
    height: 570px;
  }
  .brand {
    position: absolute;
    left: 70px;
    top: 110px;
    display: flex;
    align-items: center;
    gap: 22px;
  }
  .brand__mark {
    width: 96px;
    height: 96px;
    border-radius: 50%;
    border: 8px solid var(--ink);
    flex: none;
  }
  .brand__name {
    font-weight: 700;
    font-size: 42px;
    color: var(--ink);
    letter-spacing: 0.5px;
    white-space: nowrap;
  }
  .contact {
    position: absolute;
    right: 52px;
    top: 396px;
    text-align: right;
  }
  .contact__name {
    font-weight: 700;
    font-size: 29px;
    color: var(--gold);
    margin-bottom: 30px;
    margin-right: 0;
  }
  .contact__line {
    display: flex;
    justify-content: flex-end;
    align-items: center;
    gap: 10px;
    font-size: 22px;
    color: var(--light);
    height: 32px;
  }
  .contact__icon {
    width: 28px;
    height: 28px;
    flex: none;
  }
</style>
</head>
<body>
  <section class="card">
    <svg class="card__swoosh" viewBox="0 0 1000 570" aria-hidden="true">
      <path class="swoosh-gold" d="M0,404 C380,412 700,292 905,140 C730,300 420,468 0,512 Z" fill="#d3a92c"/>
      <path class="swoosh-black" d="M0,518 C410,472 770,300 1000,50 L1000,570 L0,570 Z" fill="#0a0a0a" stroke="#ffffff" stroke-width="5"/>
    </svg>

    <header class="brand">
      <span class="brand__mark"></span>
      <span class="brand__name">Corvath Holdings, LLC</span>
    </header>

    <div class="contact">
      <p class="contact__name">Marisol Brenkowitz</p>
      <p class="contact__line">
        <span>318-472-9051</span>
        <svg class="contact__icon" viewBox="0 0 28 28" aria-hidden="true">
          <circle cx="14" cy="14" r="12.5" fill="none" stroke="#d3a92c" stroke-width="2"/>
          <rect x="9.5" y="6.5" width="9" height="15" rx="1.8" fill="none" stroke="#d3a92c" stroke-width="1.8"/>
          <circle cx="14" cy="18.5" r="0.9" fill="#d3a92c"/>
        </svg>
      </p>
      <p class="contact__line">
        <span>corvathmb@mailvexo.com</span>
        <svg class="contact__icon" viewBox="0 0 28 28" aria-hidden="true">
          <circle cx="14" cy="14" r="12.5" fill="#d3a92c" stroke="#d3a92c" stroke-width="2"/>
          <rect x="7.5" y="9" width="13" height="10" fill="#0a0a0a"/>
          <path d="M7.5,9 L14,14.5 L20.5,9 M7.5,19 L12,14 M20.5,19 L16,14" fill="none" stroke="#d3a92c" stroke-width="1.3"/>
        </svg>
      </p>
    </div>
  </section>
</body>
</html>
```